Business Card Design Project

We need a business card for our IT services provider business. We provide services to small and medium business, and would like something that reflects the color scheme / branding on our recently updated website - www.tallobrix.com.au

The card type we have chosen is a matte laminated double sided configuration at 86mm x 54mm on 350 GSM cardboard.
Updates

Target Market(s)

Small and Medium Business owners

Industry/Entity Type

Business

Requirements
Must have
• *Details on all cards*

Company Name: Tallobrix Pty Ltd
ABN: 52 683 914 207
Address: 47-49 Pembury Street, Ashcombe Vale, Victoria 3172
Phone: 1300 GRAB UP
Fax: 03 9417 6258
Website: www.tallobrix.com.au
Logo/Handprint Icon

*Person Specific*

```html
<!DOCTYPE html>
<html lang="en">
<head>
<meta charset="utf-8">
<title>Tallobrix Business Card</title>
<link rel="stylesheet" href="https://fonts.googleapis.com/css2?family=Open+Sans:wght@400;600&display=swap">
<style>
  :root {
    --brand-blue: #3a7cab;
    --card-white: #ffffff;
    --ink-grey: #4a4a4a;
    --soft-grey: #666666;
    --backdrop: #d8d5d1;
    --font-text: "Open Sans", Arial, sans-serif;
  }
  * { box-sizing: border-box; margin: 0; padding: 0; }
  html, body { width: 1200px; height: 900px; overflow: hidden; }
  body { background: var(--backdrop); font-family: var(--font-text); position: relative; }

  .card {
    position: absolute;
    width: 560px;
    height: 352px;
    background: var(--card-white);
    box-shadow: 0 3px 10px rgba(0,0,0,0.18);
    overflow: hidden;
  }
  .card--front { left: 80px; top: 100px; }
  .card--back { left: 600px; top: 470px; }

  .logo-band {
    position: absolute;
    background: var(--brand-blue);
    display: flex;
    align-items: center;
    justify-content: center;
    gap: 12px;
  }
  .logo-name {
    color: var(--card-white);
    font-family: var(--font-text);
    font-weight: 400;
    letter-spacing: 0.04em;
  }
  .logo-mark { background: var(--card-white); }

  .card--front .logo-band { left: 0; top: 108px; width: 284px; height: 112px; }
  .card--front .logo-name { font-size: 34px; }
  .card--front .logo-mark { width: 14px; height: 14px; }

  .person {
    position: absolute;
    right: 42px;
    top: 46px;
    text-align: right;
    color: var(--ink-grey);
  }
  .person-name { font-size: 27px; font-weight: 400; margin-bottom: 16px; }
  .person-line { font-size: 13px; color: var(--soft-grey); }
  .person-line + .person-line { margin-top: 28px; }

  .company-footer {
    position: absolute;
    left: 0; right: 0;
    bottom: 26px;
    text-align: center;
    color: var(--soft-grey);
    font-size: 11px;
    line-height: 1.45;
  }
  .company-name { font-size: 13px; color: var(--ink-grey); }

  .card--back .side-strip {
    position: absolute;
    left: 0; top: 0;
    width: 36px; height: 100%;
    background: var(--brand-blue);
  }
  .website {
    position: absolute;
    left: 18px;
    top: 110px;
    transform: translate(-50%, -50%) rotate(-90deg);
    color: var(--card-white);
    font-size: 13px;
    white-space: nowrap;
  }
  .card--back .logo-band { left: 138px; right: 0; top: 74px; height: 156px; }
  .card--back .logo-name { font-size: 50px; }
  .card--back .logo-mark { width: 20px; height: 20px; }
</style>
</head>
<body>
  <section class="card card--front" aria-label="Business card front">
    <div class="logo-band">
      <span class="logo-mark" aria-hidden="true"></span>
      <span class="logo-name">Tallobrix</span>
    </div>
    <div class="person">
      <p class="person-name">Marcus Hale</p>
      <p class="person-line">phone: 9417 2915</p>
      <p class="person-line">marcus.hale@tallobrix.au</p>
    </div>
    <div class="company-footer">
      <p class="company-name">Tallobrix Pty Ltd</p>
      <p>47-49 Pembury Street, Ashcombe Vale, Victoria 3172. ABN: 52 683 914 207</p>
      <p>phone: 1300 GRAB UP&nbsp; fax: 03 9417 6258</p>
    </div>
  </section>

  <section class="card card--back" aria-label="Business card back">
    <div class="side-strip">
      <span class="website">www.tallobrix.com.au</span>
    </div>
    <div class="logo-band">
      <span class="logo-mark" aria-hidden="true"></span>
      <span class="logo-name">Tallobrix</span>
    </div>
  </section>
</body>
</html>
```